Webdesign für Honigmanufaktur
Zielgruppe
Imkerei, Verkauf von Honig und Honigerzeugnissen, so wie Bienenwachskerzen.
Zielgruppe sind vermutlich Frauen im mittleren bis gehobenen Alter.
Aufgabenstellung
Es gibt ein Firmenlogo.
Ich bevorzuge als Grundfarbe weiß, lasse mich aber von guten Einfällen gerne überraschen.
Die Website www.velunda.at finde ich sehr ansprechend.
Nur ohne Musik.
Ohne Deutsch/Englisch Auswahl.
Es soll danach Word press verwendet werden.

```html
<!DOCTYPE html>
<html lang="de">
<head>
<meta charset="utf-8">
<title>Honighof Lindenau</title>
<link rel="stylesheet" href="https://fonts.googleapis.com/css2?family=Tinos&family=Fira+Sans+Condensed:wght@400;500&family=Alegreya+Sans:ital,wght@0,400;1,400&family=Oswald:wght@500&display=swap">
<style>
:root{
  --bg:#fdfdfd;
  --orange:#e5820f;
  --brown:#3a2108;
  --text:#3b2a1c;
  --line:#d6d6d6;
  --peach:#fde8d2;
  --honey-light:#f7c948;
  --honey-dark:#d9880f;
}
*{margin:0;padding:0;box-sizing:border-box}
html,body{width:859px;height:1200px;overflow:hidden;background:var(--bg)}
body{position:relative;font-family:"Alegreya Sans",sans-serif;color:var(--text)}
.abs{position:absolute}
.nav-line{position:absolute;top:116px;height:1px;background:#e6e6e6;width:298px}
.nav a{position:absolute;top:98px;font-family:"Tinos",serif;font-size:12px;color:var(--brown);text-decoration:none;letter-spacing:.2px}
.nav a.active{color:var(--orange)}
.brand{left:355px;top:0;width:149px;height:130px;background:#fff;display:flex;flex-direction:column;align-items:center;justify-content:flex-end;padding-bottom:18px;gap:8px}
.brand-dot{width:44px;height:44px;border-radius:50%;background:var(--orange)}
.brand-name{font-family:"Oswald",sans-serif;font-weight:500;font-size:16px;color:var(--brown);letter-spacing:.6px;white-space:nowrap}
.hero-band{left:131px;top:186px;width:597px;height:269px;background:var(--peach)}
.hero-photo{left:268px;top:141px;width:321px;height:373px;background:radial-gradient(ellipse at 50% 55%,var(--honey-light) 0%,#f0b323 40%,rgba(240,179,35,.35) 62%,rgba(255,255,255,0) 75%);opacity:.9}
.hero-title{left:131px;width:597px;top:276px;text-align:center;font-family:"Tinos",serif;font-size:48px;color:var(--brown);letter-spacing:1px;line-height:1}
.hero-sub{left:131px;width:597px;top:336px;text-align:center;font-family:"Tinos",serif;font-size:18px;color:var(--brown)}
.arrow{top:299px;width:27px;height:42px;background:#fff;display:flex;align-items:center;justify-content:center}
.arrow.prev{left:131px;border-radius:0 21px 21px 0}
.arrow.next{left:701px;border-radius:21px 0 0 21px}
.divider{left:131px;width:597px;height:1px}
.divider::before,.divider::after{content:"";position:absolute;top:0;height:1px;width:278px;background:var(--line)}
.divider::before{left:0}.divider::after{right:0}
.divider span{position:absolute;left:289px;top:-10px;width:20px;height:20px;border-radius:50%;border:2px solid #f3b567}
.card{top:621px;width:137px;height:178px;border:1px solid #ececec;background:#fff}
.card-img{position:absolute;left:32px;top:-36px;width:72px;height:72px;border-radius:50%;border:2px solid var(--orange)}
.card h3{position:absolute;top:52px;width:100%;text-align:center;font-family:"Fira Sans Condensed",sans-serif;font-weight:500;font-size:12.5px;color:var(--brown)}
.card p{position:absolute;left:8px;right:8px;top:76px;font-size:7px;line-height:8.7px;text-align:justify;color:var(--text)}
.card .btn{position:absolute;left:27px;top:140px;width:76px;height:20px;background:var(--orange);color:#fff;font-style:italic;font-size:7px;display:flex;align-items:center;justify-content:center}
.video{left:134px;top:923px;width:269px;height:158px;background:linear-gradient(160deg,#eef0ee 0%,#c9c58a 45%,#6d7140 75%,#3a3422 100%);box-shadow:0 4px 14px rgba(0,0,0,.15)}
.play{position:absolute;left:117px;top:61px;width:36px;height:36px;border-radius:50%;background:rgba(40,30,20,.65);display:flex;align-items:center;justify-content:center}
.about-title{left:451px;width:277px;top:926px;text-align:center;font-family:"Fira Sans Condensed",sans-serif;font-weight:500;font-size:12.5px;color:var(--orange)}
.about-text{left:451px;width:277px;top:950px;font-size:7.6px;line-height:13.7px;text-align:justify;letter-spacing:.2px}
.follow{left:453px;top:1062px;display:flex;align-items:center;gap:5px;font-size:7px;font-style:italic;color:#6b6b6b}
.follow .gap{width:8px}
.social{width:11px;height:11px;border-radius:50%}
.footer-links{left:0;width:859px;top:1141px;text-align:center;font-size:6px;color:var(--brown);letter-spacing:.2px}
.copy{left:0;width:859px;top:1152px;text-align:center;font-size:5.5px;color:#9a9a9a}
.top-btn{left:413px;top:1173px;width:31px;height:27px;background:var(--orange);color:#fff;font-size:5px;display:flex;flex-direction:column;align-items:center;justify-content:center;gap:2px}
</style>
</head>
<body>
<div class="nav-line" style="left:34px"></div>
<div class="nav-line" style="left:528px"></div>
<nav class="nav">
  <a class="active" style="left:67px">MANUFAKTUR</a>
  <a style="left:182px">TEAM</a>
  <a style="left:248px">HONIG</a>
  <a style="left:558px">BIENENWACHS</a>
  <a style="left:676px">SHOP</a>
  <a style="left:741px">KONTAKT</a>
</nav>
<div class="abs brand"><div class="brand-dot"></div><div class="brand-name">HONIGHOF LINDENAU</div></div>

<div class="abs hero-band"></div>
<div class="abs hero-photo" role="img" aria-label="Honigglas mit Honiglöffel"></div>
<h1 class="abs hero-title">GESCHMACK</h1>
<p class="abs hero-sub">macht den Unterschied</p>
<div class="abs arrow prev"><svg width="8" height="10" viewBox="0 0 8 10"><path d="M6 1 2 5l4 4" fill="none" stroke="#111" stroke-width="1.8"/></svg></div>
<div class="abs arrow next"><svg width="8" height="10" viewBox="0 0 8 10"><path d="M2 1l4 4-4 4" fill="none" stroke="#111" stroke-width="1.8"/></svg></div>

<div class="abs divider" style="top:536px"><span></span></div>

<section>
  <div class="abs card" style="left:131px"><div class="card-img" role="img" aria-label="Löffel mit fließendem Honig" style="background:radial-gradient(circle at 55% 60%,#e0a431,#f4efe6 60%)"></div><h3>Unser Honig</h3><p>Lorem ipsum dolor sit amet, consetetur sadipscing elitr, sed diam nonumy eirmod tempor inviduntLorem ipsum dolor sit amet, consetetur sadipscing elitr, sed diam nonumy eirmod tempor invidunt consetetur sadips.</p><div class="btn">Mehr erfahren</div></div>
  <div class="abs card" style="left:286px"><div class="card-img" role="img" aria-label="Biene auf einer Blüte" style="background:radial-gradient(circle at 55% 60%,#b56a1e,#e9ecef 65%)"></div><h3>Unser Team</h3><p>Lorem ipsum dolor sit amet, consetetur sadipscing elitr, sed diam nonumy eirmod tempor inviduntLorem ipsum dolor sit amet, consetetur sadipscing elitr, sed diam nonumy eirmod tempor invidunt consetetur sadips.</p><div class="btn">Mehr erfahren</div></div>
  <div class="abs card" style="left:441px"><div class="card-img" role="img" aria-label="Bienen auf Wabe" style="background:radial-gradient(circle,#8a5a2b,#5a3516)"></div><h3>Unser Bienenwachs</h3><p>Lorem ipsum dolor sit amet, consetetur sadipscing elitr, sed diam nonumy eirmod tempor inviduntLorem ipsum dolor sit amet, consetetur sadipscing elitr, sed diam nonumy eirmod tempor invidunt consetetur sadips.</p><div class="btn">Mehr erfahren</div></div>
  <div class="abs card" style="left:597px"><div class="card-img" role="img" aria-label="Honiggläser" style="background:radial-gradient(circle,#ef9a1c 0%,#f5b73c 35%,#fff 62%)"></div><h3>Unser Shop</h3><p>Lorem ipsum dolor sit amet, consetetur sadipscing elitr, sed diam nonumy eirmod tempor inviduntLorem ipsum dolor sit amet, consetetur sadipscing elitr, sed diam nonumy eirmod tempor invidunt consetetur sadips.</p><div class="btn">Mehr erfahren</div></div>
</section>

<div class="abs divider" style="top:861px"><span></span></div>

<div class="abs video" role="img" aria-label="Video: Imker mit Wabenrahmen zwischen Blumen"><div class="play"><svg width="12" height="12" viewBox="0 0 12 12"><path d="M3 1.5v9l7.5-4.5z" fill="#fff"/></svg></div></div>
<h2 class="abs about-title">HONIGHOF LINDENAU</h2>
<p class="abs about-text">Lorem ipsum dolor sit amet, consetetur sadipscing elitr, sed diam nonumy eirmod tempor inviduntLorem ipsum dolor sit amet, consetetur sadipscing elitr, sed diam nonumy eirmod tempor invidunt consetetur sadips..Lorem ipsum dolor sit amet, consetetur sadipscing elitr, sed diam nonumy eirmod tempor inviduntLorem ipsum dolor sit amet, consetetur sadipscing elitr, sed diam nonumy eirmod tempor invidunt consetetur sadips..Lorem ipsum dolor sit amet, consetetu ipsum dolor.</p>
<div class="abs follow">Folge uns auf:<span class="gap"></span>
  <span class="social" style="background:#5a74b0"></span>
  <span class="social" style="background:#e0232a"></span>
  <span class="social" style="background:#6cb7e6"></span>
  <span class="social" style="background:#2e7bb4"></span>
  <span class="social" style="background:#e87b6e"></span>
</div>

<footer>
  <div class="abs footer-links">IMPRESSUM | DATENSCHUTZ | AGB | SITEMAP | KONTAKT</div>
  <div class="abs copy">©2018 Honighof Lindenau</div>
  <div class="abs top-btn"><svg width="8" height="5" viewBox="0 0 8 5"><path d="M1 4l3-3 3 3" fill="none" stroke="#fff" stroke-width="1.3"/></svg>Nach oben</div>
</footer>
</body>
</html>
```